New Restaurant Menu - Lane 48

I'm looking for a MENU design with a particular feel.  I want to have a base template made that I can then use for future alterations to the menu; ie  I can go in and change out different entrees as the menu changes but the template will remain the same.  The restaurants name is "Lane 48".  It is based off an old secret subway station underneath the Brennley Ashcourt in NYC.  The logo will look similar to a tile mosaic that you would see in NYC at a subway station.  I've attached the logo that will appear in tile throughout the restaurant.  A menu that I really like that inspires me is the menu from a restaurant called "Grey Lantern" in San Francisco.  I suggest that you visit their website and take a look at their menu to get a feel for what it is that I like.
http://greylanternsf.example/wp-content/uploads/2018/01/011018-Quick-Menu.pdf
Target Market(s)
The restaurant is will feature NYC Street art and serve Italian inspired food. Dorin Velsk does a painting of Alba Marenti that will be in the restaurant. For lack of a better way of saying this, we are looking for a design that would make people think an artist developed it.
#3277b5
#85acd3
#cedeed
#0355a3
Menu Design Requirements
Must Have:
- This project must come original. Imagine a restaurant that was carved out of a secret subway station.
Nice to Have:
- I would like to see a design that makes you think an italian artist/graphic designer perhaps a street artist designed the menu.

Target Market(s)
25-35 year old restaurant crowd
Industry/Entity Type
Restaurant
Requirements
Must have
- I want a menu! I am not looking for logo design! I've attached a menu template from a restaurant that you can draw inspiration from. Take a look at it.

Nice to have
- I want a menu template. I've attached a semi completed menu of the items I want to sell. I do not want a logo! I want a menu design.

```html
<!DOCTYPE html>
<html lang="en">
<head>
<meta charset="utf-8">
<title>Lane 48 Menu</title>
<link rel="stylesheet" href="https://fonts.googleapis.com/css2?family=Cinzel:wght@400;600&family=Sorts+Mill+Goudy&display=swap">
<style>
:root{
  --page:#eef2f3;
  --sheet:#5a9ea4;
  --panel:#3f7f87;
  --panel-dark:#2f6a72;
  --rule:#a9dade;
  --plaque:#6fb3b9;
  --plaque-edge:#cfeff0;
  --ink:#ffffff;
  --ink-soft:#d6ecee;
  --leader:#bfe1e3;
}
*{box-sizing:border-box;margin:0;padding:0}
html,body{width:774px;height:1200px;overflow:hidden}
body{background:var(--page);font-family:"Sorts Mill Goudy",Georgia,serif;color:var(--ink);position:relative}
.sheet{position:absolute;left:20px;width:734px;height:565px;background:var(--sheet);padding:7px;display:grid;grid-template-columns:1fr 1fr 1fr;gap:6px}
.sheet--front{top:20px}
.sheet--back{top:612px}
.panel{background:linear-gradient(180deg,var(--panel) 0%,var(--panel-dark) 100%);border:1px solid var(--rule);box-shadow:inset 0 0 0 3px var(--panel),inset 0 0 0 4px var(--rule);padding:24px 14px 14px;position:relative;overflow:hidden}
.crest{position:absolute;top:5px;left:50%;transform:translateX(-50%);width:90px;height:12px;background:linear-gradient(90deg,transparent,var(--plaque) 30%,var(--plaque) 70%,transparent);opacity:.7}
.plaque{display:block;width:120px;margin:4px auto 8px;border:1px solid var(--plaque-edge);background:var(--plaque);box-shadow:inset 0 0 0 2px var(--plaque),inset 0 0 0 3px var(--plaque-edge);font-family:"Cinzel",serif;font-size:11px;letter-spacing:.5px;text-align:center;padding:6px 4px;line-height:1.1;color:var(--ink)}
.item{display:flex;align-items:baseline;font-size:7.6px;font-weight:bold;line-height:1.25;margin-top:2px}
.item .name{white-space:nowrap}
.item .leader{flex:1;border-bottom:1px dotted var(--leader);margin:0 3px;transform:translateY(-1px)}
.item .price{white-space:nowrap;font-weight:normal}
.desc{font-size:6.8px;line-height:1.22;color:var(--ink-soft)}
.note{font-size:7px;text-align:center;line-height:1.3;margin:2px 0 4px}
.note em{font-style:italic}
.unit{font-size:6.8px;text-align:right}
.brand{display:flex;align-items:center;justify-content:center;gap:5px;width:110px;margin:10px auto 14px;border:1px solid var(--plaque-edge);background:var(--panel-dark);padding:4px;font-family:"Cinzel",serif;font-size:11px;color:var(--ink)}
.brand i{width:7px;height:7px;background:var(--ink)}
.story{font-size:8.4px;line-height:1.38;text-align:center;color:var(--ink-soft);margin-bottom:9px}
.photo{position:absolute;left:4px;right:4px;bottom:4px;height:210px;background:linear-gradient(180deg,var(--panel-dark) 0%,#6a9ca2 45%,#24545b 100%)}
.entree{text-align:center;margin-bottom:10px}
.entree h3{font-size:8.2px;font-weight:bold}
.entree p{font-size:7.6px;line-height:1.25;color:var(--ink-soft)}
.two-col{display:grid;grid-template-columns:1fr 1fr;font-size:7.4px;line-height:1.4;padding:0 8px;margin-bottom:8px}
.two-col span:nth-child(even){text-align:right}
.wine .price{font-size:6.6px}
.gap{height:6px}
</style>
</head>
<body>

<section class="sheet sheet--front">
  <article class="panel">
    <div class="crest" role="img" aria-label="Scrolled ornament crest"></div>
    <h2 class="plaque">Appetizers</h2>
    <div class="item"><span class="name">Arancini (Italian rice balls)</span><span class="leader"></span><span class="price">10</span></div>
    <p class="desc">Cheesy risotto balls deep fried and served with marinara sauce</p>
    <div class="item"><span class="name">Antipasto</span><span class="leader"></span><span class="price">16</span></div>
    <p class="desc">imported cheeses, cured meats, peppadew peppers, and balsamic roasted eggplant</p>
    <div class="item"><span class="name">Fried Bocconcini</span><span class="leader"></span><span class="price">11</span></div>
    <p class="desc">made with fresh mozzarella cheese and homemade marinara sauce</p>
    <div class="item"><span class="name">Mint and Basil Pesto Shrimp</span><span class="leader"></span><span class="price">12</span></div>
    <p class="desc">served with a side of avocado cumin sauce</p>
    <div class="item"><span class="name">Grilled Scallops</span><span class="leader"></span><span class="price">8.50</span></div>
    <p class="desc">served over a sautéed creamy corn relish</p>
    <div class="item"><span class="name">Eggplant Rollatini</span><span class="leader"></span><span class="price">5</span></div>
    <p class="desc">thinly sliced grilled eggplant drizzled with pesto and stuffed with creamy ricotta cheese and spinach</p>
    <div class="item"><span class="name">Creamy Spinach Dip</span><span class="leader"></span><span class="price">9.75</span></div>
    <p class="desc">served hot with grilled Italian bread</p>
    <div class="item"><span class="name">Bruschetta</span><span class="leader"></span><span class="price">7.75</span></div>
    <p class="desc">grilled Italian bread topped with tomatoes, basil, garlic, parmesan and olive oil</p>
    <h2 class="plaque" style="margin-top:12px">Salads</h2>
    <p class="note">(small/large)<br>Add grilled shrimp 3.50 / 5<br>Add grilled Chicken 2.50 / 4<br>Add Flank Steak 4.25 / 6</p>
    <div class="item"><span class="name">Lane 48 Salad</span><span class="leader"></span><span class="price">6.95 / 10.25</span></div>
    <p class="desc">Kale with sliced almonds, Pecorino Romano, candied fig, pancetta and lemon sesame dressing</p>
    <div class="item"><span class="name">Mediterranean Salad</span><span class="leader"></span><span class="price">6.95 / 10.25</span></div>
    <p class="desc">with green leaf lettuce, fresh mozzarella, garbanzo beans, tomatoes, cucumbers, bell peppers, onions and balsamic vinaigrette</p>
    <div class="item"><span class="name">Chicken Caesar Salad</span><span class="leader"></span><span class="price">10.50</span></div>
    <p class="desc">with romaine lettuce, pecorino romano, garlic knot croutons and Caesar dressing</p>
    <div class="item"><span class="name">Grilled Flat Iron Steak</span><span class="leader"></span><span class="price">14.50</span></div>
    <p class="desc">salad with avocado, blue cheese, sliced almonds, garbanzo beans and candied bacon served with a creamy Garlic roasted dressing</p>
    <div class="item"><span class="name">Apple and Brie Salad</span><span class="leader"></span><span class="price">11</span></div>
    <p class="desc">with candied walnuts, arugula, pancetta, and balsamic vinaigrette</p>
  </article>

  <article class="panel">
    <div class="crest" role="img" aria-label="Scrolled ornament crest"></div>
    <h1 class="brand"><i></i>LANE 48</h1>
    <p class="story">Lane 48 is a secret train track under the Brennley Ashcourt in NYC that was built for private train cars to enter directly into the hotel where they could take a private freight elevator directly into the building.</p>
    <p class="story">General Harlan Mercer was the first to use this secret track during world war 1. President Ellis Vantor used the track to conceal his paralysis from the public when he traveled to New York in 1944. Rumor has it that Otto Brandlin threw an underground party there in 1965. The track was also prepped for a visit by Walter Ashby when he attended a meeting at the hotel. Fun fact: it takes 7 minutes to get from lane 48 to Kessel Field airport.</p>
    <div class="photo" role="img" aria-label="Photograph of an old rail car standing in the hidden underground track"></div>
  </article>

  <article class="panel">
    <div class="crest" role="img" aria-label="Scrolled ornament crest"></div>
    <h2 class="plaque">Soups</h2>
    <p class="unit">Cup / Bowl</p>
    <div class="item"><span class="name">Pasta Fagioli</span><span class="leader"></span><span class="price">4 / 8</span></div>
    <p class="desc">ditalini pasta, veggies and beans in a chicken broth sprinkled with freshly grated pecorino romano cheese</p>
    <div class="item"><span class="name">Chicken Noodle Soup</span><span class="leader"></span><span class="price">4.25 / 8.50</span></div>
    <p class="desc">home style chicken soup with ditalini pasta</p>
    <h2 class="plaque" style="margin-top:10px">Sides</h2>
    <div class="item"><span class="name">Caprese Salad</span><span class="leader"></span><span class="price">4</span></div>
    <p class="desc">drizzled with balsamic reduction</p>
    <div class="item"><span class="name">Couscous Salad</span><span class="leader"></span><span class="price">3</span></div>
    <p class="desc">with fresh veggies, garbanzos and feta cheese</p>
    <div class="item"><span class="name">Parmesan fries</span><span class="leader"></span><span class="price">3</span></div>
    <div class="item"><span class="name">Homemade chips</span><span class="leader"></span><span class="price">3</span></div>
    <div class="item"><span class="name">Garlic knots</span><span class="leader"></span><span class="price">3</span></div>
    <h2 class="plaque" style="margin-top:10px">Sandwiches</h2>
    <p class="note">All Sandwiches are served hot<br>and can add candied bacon or cheese 1.50</p>
    <div class="item"><span class="name">Italian Hero</span><span class="leader"></span><span class="price">10.50</span></div>
    <p class="desc">Salami, Capicola, Pancetta, Ham, peppadew peppers, pickled onions, melted provolone, Oregano, lettuce and tomatoes with Dijon vinaigrette on a fresh baguette</p>
    <div class="item"><span class="name">Grilled Flat Iron Steak</span><span class="leader"></span><span class="price">11.50</span></div>
    <p class="desc">served on a baguette with garlic aioli, grilled onions and arugula</p>
    <div class="item"><span class="name">Adult Grilled Cheese</span><span class="leader"></span><span class="price">7.95</span></div>
    <p class="desc">with cheddar, provolone, gruyere, tomato and avocado</p>
    <div class="item"><span class="name">Candied Bacon Burger</span><span class="leader"></span><span class="price">9.75</span></div>
    <p class="desc">with melted provolone cheese, avocado, arugula and pickled onion</p>
    <div class="item"><span class="name">Home style Fried or Grilled Chicken Breast</span><span class="leader"></span><span class="price">9.50</span></div>
    <p class="desc">with garlic aioli, arugula, melted gruyere, Dijon vinaigrette and pickled onions</p>
    <div class="item"><span class="name">Grilled Veggies</span><span class="leader"></span><span class="price">7.95</span></div>
    <p class="desc">bell peppers, spinach, mushrooms, eggplant with fresh mozzarella and pesto served on a fresh baguette</p>
    <div class="item"><span class="name">Turkey and Melted Brie</span><span class="leader"></span><span class="price">9.50</span></div>
    <p class="desc">roasted apple, arugula with Dijon vinaigrette on a fresh baguette</p>
  </article>
</section>

<section class="sheet sheet--back">
  <article class="panel">
    <div class="crest" role="img" aria-label="Scrolled ornament crest"></div>
    <h2 class="plaque">Entrees</h2>
    <p class="note" style="font-size:7.6px;margin-bottom:12px">Add shrimp 6<br>Add meatballs 5<br>Add Chicken 4.50</p>
    <div class="entree"><h3>Seared Redfish • 24</h3><p>served over a sautéed creamy corn relish and wilted spinach</p></div>
    <div class="entree"><h3>Grilled Flat Iron Steak • 26</h3><p>served with sautéed mushrooms, parmesan fries and wilted spinach</p></div>
    <div class="entree"><h3>6 oz Filet • 28</h3><p>with parmesan fries and balsamic roasted eggplant</p></div>
    <div class="entree"><h3>Chicken Marsala • 16</h3><p>lightly fried chicken breast marinated in Marsala wine and mushrooms served over linguine</p></div>
    <div class="entree"><h3>Fettuccine Alfredo • 16/18</h3><p>buttery and creamy fettucine with chicken or shrimp</p></div>
    <div class="entree"><h3>Eggplant Parmesan • 12</h3><p>fried eggplant stacked with layers of feta, mozzarella, and basil and served over marinara sauce</p></div>
    <div class="entree"><h3>Penne alla Vodka • 13</h3><p>light, tangy and creamy tomato sauce served over penne pasta</p></div>
    <div class="entree"><h3>Homemade Marinara • 9</h3><p>basil, olive oil, with pecorino Romano served with your choice of pasta</p></div>
    <div class="entree"><h3>Traditional Spaghetti and Meatballs • 14</h3><p>classic spaghetti with traditional beef meatballs</p></div>
    <p class="note"><em>*All Entrees are served only during dinner hours*</em></p>
  </article>

  <article class="panel">
    <div class="crest" role="img" aria-label="Scrolled ornament crest"></div>
    <h2 class="plaque">Dessert</h2>
    <div class="item"><span class="name">Tiramisu</span><span class="leader"></span><span class="price">8</span></div>
    <div class="item"><span class="name">New York Style Cheesecake</span><span class="leader"></span><span class="price">8</span></div>
    <div class="item"><span class="name">Chocolate Chip Cannoli</span><span class="leader"></span><span class="price">4 each</span></div>
    <div class="item"><span class="name">Giant Chewy Chocolate Chip and Walnut Cookies</span><span class="leader"></span><span class="price">3.50 each</span></div>
    <div class="item"><span class="name">Chewy Lemon Ricotta Cookies</span><span class="leader"></span><span class="price">3.50 each</span></div>
    <p class="desc">with lemon glaze</p>
    <p class="note" style="margin-top:8px"><em>Consuming raw or undercooked meats, poultry, seafood,<br>shellfish, or eggs may increase your risk of foodborne illness.</em></p>
    <h2 class="plaque" style="margin-top:10px">Fountain Beverages</h2>
    <p class="note">Fizzo, Diet Fizzo, Dr. Bramble, Limelet</p>
    <div class="gap"></div>
    <div class="item"><span class="name">Mint Lemonade</span><span class="leader"></span><span class="price">2.99</span></div>
    <div class="item"><span class="name">Iced Tea</span><span class="leader"></span><span class="price">1.99</span></div>
    <div class="item"><span class="name">Coffee</span><span class="leader"></span><span class="price">2.75</span></div>
    <h2 class="plaque" style="margin-top:10px">Domestic Beer</h2>
    <div class="two-col">
      <span>Hollis Pils</span><span>Marrow Gold Light</span>
      <span>Hollis Light</span><span>Kettle Ridge Ultra</span>
      <span>Cobb Creek Light</span><span>Pinecastle Lager</span>
    </div>
    <h2 class="plaque">Imported Beer</h2>
    <div class="two-col">
      <span>Veldhaven Blonde</span><span>Bayou Copper</span>
      <span>Castagna</span><span>Marshland Dark</span>
      <span>Rusty Gate Bock</span><span>Dotty B</span>
      <span>Highmeadow Pale Ale</span><span>Redwood Trail IPA</span>
      <span>Solmar Light</span><span>Tumbleweed Amber Ale</span>
      <span>Orchard Wit</span><span>Dunmore Stout</span>
    </div>
  </article>

  <article class="panel">
    <div class="crest" role="img" aria-label="Scrolled ornament crest"></div>
    <h2 class="plaque">Specialty Cocktails</h2>
    <div class="item"><span class="name">Sangria</span><span class="leader"></span><span class="price">$</span></div>
    <p class="desc">Red Sparkling Wine served with a variety of fresh fruits</p>
    <h2 class="plaque" style="margin-top:16px">Sparkling</h2>
    <div class="item wine"><span class="name">Cantina Vessa</span><span class="leader"></span><span class="price">$ half glass $ glass $ bottle</span></div>
    <p class="desc">Corvello Brut, Italy</p>
    <h2 class="plaque" style="margin-top:16px">White Wines</h2>
    <div class="item wine"><span class="name">The Regent</span><span class="leader"></span><span class="price">$ half glass $ glass $ bottle</span></div>
    <p class="desc">Chenin Blanc, South Africa</p>
    <div class="item wine"><span class="name">Villa Q</span><span class="leader"></span><span class="price">$ half glass $ glass $ bottle</span></div>
    <p class="desc">Pinot Gris, Germany</p>
    <h2 class="plaque" style="margin-top:16px">Red Wines</h2>
    <div class="item wine"><span class="name">Domaine de Castelmor</span><span class="leader"></span><span class="price">$ half glass $ glass $ bottle</span></div>
    <p class="desc">80% Grenache, 15% Syrah, 5% Carignan, France</p>
    <div class="item wine"><span class="name">Harrow Family Reserve</span><span class="leader"></span><span class="price">$ half glass $ glass $ bottle</span></div>
    <p class="desc">60% Cabernet Sauvignon, 35% Merlot, 5% Malbec<br>Washington State</p>
    <div class="item wine"><span class="name">Velvet Cocoa</span><span class="leader"></span><span class="price">$ half glass $ glass $ bottle</span></div>
    <p class="desc">Syrah/Malbec Blend, California</p>
    <div class="item wine"><span class="name">Harrow Stone Hill</span><span class="leader"></span><span class="price">$ half glass $ glass $ bottle</span></div>
    <p class="desc">Cabernet Sauvignon, Washington State</p>
    <div class="item wine"><span class="name">Quill Creek Syrah</span><span class="leader"></span><span class="price">$ half glass $ glass $ bottle</span></div>
    <p class="desc">Syrah, Washington State</p>
    <div class="item wine"><span class="name">Marco &amp; Silvio</span><span class="leader"></span><span class="price">$ half glass $ glass $ bottle</span></div>
    <p class="desc">Pinot Noir, California</p>
  </article>
</section>

</body>
</html>
```